House-share and Room Rental Website (With Focus on the Bedroom Landing Page)

Looking for website design for our House-share (executive accommodation) and room rental business.

Our company name is: Lodvenra could also be written as LodVenra or lodvenra. Either is fine .. just looking for a nice clean catchy logo to go with the design.

EXAMPLES
These are examples of other websites in this field that are doing well. this is a kind of baseline.
https://kelbrin.com.au/
https://www.tuvaplex.com/
https://www.nestorvi.com/
https://www.quillsa.net/
https://www.pendlebarrow.com.au/

Our business model is to rent rooms to people looking for high-quality accommodation. We fill the gap between those looking to rent rooms and those with rooms to rent. However, our model is slightly different from those already on the market as we looking to fill a massive gap in the market delivering upmarket rooms for rent.(Executive Accommodation) also in the back end will be coupled with a self management process in the back end.

We offer executive style accommodation that stands out above the rest. With special extras like fire safety.. and management processes that create happier homes. We are looking for a web design package that can help us grow and scale our business. We need a design that is captivating

Our MAIN focus is having a room landing page that stands out from the rest... The core of our business will rely on the promotion of the rooms in a share house... so the whole design relies on the BEDROOM landing page to drive results.

Target Market(s)

We have 2 markets we are aiming at ... the first market is people offering rooms to rent who want the highest rental return. The second market is people looking to rent safe, high-quality rooms, in houses that are well managed and looked after.

Industry/Entity Type

Share Economy

Logo Text

LodVenra

Number of Pages Required

5+ page

Font styles to use
Sans Serif

Colors
3276b5

Requirements
Must have
• A messaging system whereby we can create direct communication between those offering rooms and those looking for rooms.
• A call to action that says " Schedule an Inspection"
• Landing page for promoting rooms
• A home page for showing stock.
• Profile page for those selling rooms
• Profile page for those looking for rooms.
• A scheduling calendar for booking inspections
Nice to have
• Pages where new residents can lock in a room.. pay bond and rents.. and sign contracts
• Notifications
• SMS capabilities in the backend.
Should not have
• No script or handwriting fonts.

```html
<!DOCTYPE html>
<html lang="en">
<head>
<meta charset="utf-8">
<title>LodVenra – The white room</title>
<link rel="stylesheet" href="https://fonts.googleapis.com/css2?family=Lato:wght@300;400;700;900&display=swap">
<style>
  :root {
    --brand: #3276b5;
    --ink: #111111;
    --ink-soft: #333333;
    --muted: #b9b9b9;
    --line: #e4e4e4;
    --paper: #ffffff;
    --backdrop: #f1f2f4;
    --photo-light: #ece8e4;
    --photo-mid: #bdb3aa;
    --photo-dark: #6d5f55;
  }
  * { box-sizing: border-box; margin: 0; padding: 0; }
  html, body {
    width: 880px; height: 1200px; overflow: hidden;
    background: var(--backdrop);
    font-family: "Lato", Arial, sans-serif;
    color: var(--ink);
  }
  .room-page {
    position: absolute; left: 151px; top: 8px;
    width: 578px; height: 1184px;
    background: var(--paper);
    overflow: hidden;
  }
  .site-header {
    position: absolute; left: 0; top: 0; width: 100%; height: 61px;
    display: flex; align-items: center; justify-content: space-between;
    padding: 0 22px 0 24px;
  }
  .brand { display: flex; align-items: center; gap: 10px; }
  .brand-square { width: 16px; height: 16px; background: var(--brand); }
  .brand-name { font-weight: 900; font-size: 30px; color: var(--ink); letter-spacing: -0.2px; }
  .header-actions { display: flex; align-items: center; gap: 28px; }
  .room-photo {
    position: absolute; left: 0; top: 61px; width: 100%; height: 408px;
    background:
      radial-gradient(ellipse at 50% 85%, #f7f6f4 0%, #e3dfdb 35%, transparent 60%),
      linear-gradient(180deg, var(--photo-light) 0%, var(--photo-mid) 45%, var(--photo-dark) 62%, #e6e3df 78%, #d2cdc8 100%);
  }
  .room-city {
    position: absolute; left: 12px; top: 494px;
    font-size: 21px; font-weight: 700; letter-spacing: 0.2px;
  }
  .room-title {
    position: absolute; left: 11px; top: 530px;
    font-size: 54px; font-weight: 300; letter-spacing: -0.5px; line-height: 1.15;
  }
  .room-type {
    position: absolute; left: 12px; top: 594px;
    font-size: 31px; font-weight: 900; letter-spacing: -0.2px;
  }
  .rating {
    position: absolute; left: 12px; top: 640px;
    display: flex; align-items: center; gap: 4px;
    font-size: 21px; color: var(--ink-soft);
  }
  .rating svg { width: 27px; height: 26px; fill: var(--brand); }
  .rating-count { margin-left: 4px; }
  .room-description {
    position: absolute; left: 12px; top: 678px; width: 546px;
    font-size: 23px; line-height: 37px; color: var(--ink);
  }
  .features {
    position: absolute; left: 0; top: 930px; width: 100%;
    display: flex; justify-content: space-between; padding: 0 6px 0 12px;
  }
  .feature { width: 108px; text-align: center; }
  .feature svg { width: 34px; height: 34px; stroke: var(--ink-soft); fill: none; stroke-width: 1.6; }
  .feature-label { font-size: 8px; letter-spacing: 0.3px; color: var(--muted); text-transform: uppercase; margin-top: 3px; }
  .feature-value { font-size: 19px; color: var(--ink-soft); margin-top: 1px; }
  .features-more { top: 1040px; }
  .price-bar {
    position: absolute; left: 0; top: 1064px; width: 100%; height: 120px;
    background: var(--paper); border-top: 1px solid var(--line);
  }
  .price-label { position: absolute; left: 24px; top: 18px; font-size: 18px; color: var(--ink-soft); }
  .price-amount { position: absolute; left: 23px; top: 42px; font-size: 48px; font-weight: 700; color: var(--brand); letter-spacing: -0.5px; }
  .book-button {
    position: absolute; left: 295px; top: 35px; width: 258px; height: 55px;
    background: var(--brand); color: #fff; border: 1px solid #245d93;
    font-family: "Lato", Arial, sans-serif; font-size: 21px; letter-spacing: 0.5px;
    display: flex; align-items: center; justify-content: center;
  }
</style>
</head>
<body>
<main class="room-page">
  <header class="site-header">
    <div class="brand">
      <span class="brand-square"></span>
      <span class="brand-name">LodVenra</span>
    </div>
    <div class="header-actions">
      <svg width="36" height="36" viewBox="0 0 36 36" fill="none" stroke="#222" stroke-width="1.8" aria-label="Account">
        <circle cx="18" cy="11" r="8"/>
        <path d="M3 33c1-8 7-12 15-12s14 4 15 12z"/>
      </svg>
      <svg width="38" height="28" viewBox="0 0 38 28" stroke="#222" stroke-width="2" aria-label="Menu">
        <line x1="1" y1="3" x2="37" y2="3"/><line x1="1" y1="14" x2="37" y2="14"/><line x1="1" y1="25" x2="37" y2="25"/>
      </svg>
    </div>
  </header>

  <div class="room-photo" role="img" aria-label="Photo of a bright white double bedroom with grey pillows, pendant lights and a wooden breakfast tray on the bed"></div>

  <p class="room-city">MELBOURNE</p>
  <h1 class="room-title">The white room</h1>
  <h2 class="room-type">DOUBLE BEDROOM</h2>
  <div class="rating">
    <svg viewBox="0 0 24 24"><path d="M12 1.5l3.1 6.9 7.4.7-5.6 5 1.7 7.4L12 17.6 5.4 21.5l1.7-7.4-5.6-5 7.4-.7z"/></svg>
    <svg viewBox="0 0 24 24"><path d="M12 1.5l3.1 6.9 7.4.7-5.6 5 1.7 7.4L12 17.6 5.4 21.5l1.7-7.4-5.6-5 7.4-.7z"/></svg>
    <svg viewBox="0 0 24 24"><path d="M12 1.5l3.1 6.9 7.4.7-5.6 5 1.7 7.4L12 17.6 5.4 21.5l1.7-7.4-5.6-5 7.4-.7z"/></svg>
    <svg viewBox="0 0 24 24"><path d="M12 1.5l3.1 6.9 7.4.7-5.6 5 1.7 7.4L12 17.6 5.4 21.5l1.7-7.4-5.6-5 7.4-.7z"/></svg>
    <svg viewBox="0 0 24 24"><path d="M12 1.5l3.1 6.9 7.4.7-5.6 5 1.7 7.4L12 17.6 5.4 21.5l1.7-7.4-5.6-5 7.4-.7z"/></svg>
    <span class="rating-count">314</span>
  </div>
  <p class="room-description">Maecenas et ligula consectetur diam convallis posuere eget eget velit. Morbi ac augue at dolor sollicitudin rhoncus. Cras vulputate, metus at iaculis varius, tellus nisl scelerisque magna, vel consectetur elit mi id nisi. Ut blandit orci vel lectus sagittis, nec fermentum neque fringilla.</p>

  <section class="features">
    <div class="feature">
      <svg viewBox="0 0 34 34"><circle cx="17" cy="10" r="7"/><path d="M4 32c1-8 6-12 13-12s12 4 13 12z"/></svg>
      <div class="feature-label">Gender</div>
      <div class="feature-value">Single</div>
    </div>
    <div class="feature">
      <svg viewBox="0 0 34 34"><rect x="9" y="4" width="16" height="28"/><path d="M6 4h22M12 4v28"/></svg>
      <div class="feature-label">Room size</div>
      <div class="feature-value">40 Sqm</div>
    </div>
    <div class="feature">
      <svg viewBox="0 0 34 34"><rect x="6" y="3" width="8" height="14"/><path d="M6 17h22c0 6-4 9-9 9l1 6h-8l1-6c-4-1-7-4-7-9z"/></svg>
      <div class="feature-label">Bathroom</div>
      <div class="feature-value">Private</div>
    </div>
    <div class="feature">
      <svg viewBox="0 0 34 34"><rect x="5" y="3" width="24" height="28"/><path d="M13 26V9h6a4 4 0 010 8h-6"/></svg>
      <div class="feature-label">Parking</div>
      <div class="feature-value">Private</div>
    </div>
    <div class="feature">
      <svg viewBox="0 0 34 34"><circle cx="17" cy="17" r="14"/><path d="M7 27L27 7M9 17h16v4H9z"/></svg>
      <div class="feature-label">Smoking</div>
      <div class="feature-value">Not allowed</div>
    </div>
  </section>

  <section class="features features-more" aria-hidden="true">
    <div class="feature"><svg viewBox="0 0 34 34"><path d="M4 30l8-8 6 6 12-16M24 12h6v6"/></svg></div>
    <div class="feature"><svg viewBox="0 0 34 34"><rect x="4" y="6" width="26" height="20"/><path d="M10 12h5v5h-5zM19 12h5v5h-5z"/></svg></div>
    <div class="feature"><svg viewBox="0 0 34 34"><circle cx="10" cy="14" r="6"/><circle cx="24" cy="14" r="6"/></svg></div>
    <div class="feature"><svg viewBox="0 0 34 34"><rect x="11" y="4" width="12" height="26"/></svg></div>
    <div class="feature"><svg viewBox="0 0 34 34"><circle cx="17" cy="24" r="13"/></svg></div>
  </section>

  <footer class="price-bar">
    <p class="price-label">Rental price (per month)</p>
    <p class="price-amount">A$600</p>
    <div class="book-button">BOOK</div>
  </footer>
</main>
</body>
</html>
```